Electrical & Communications Company Wordpress Themed Website Design

Hi everyone,

I need a wordpress themed website designed for a new company based in Sydney Australia called "VELTRIX". It delivers electrical and communication services to the domestic and commercial sectors.

It needs to be the FULL/COMPLETE wordpress theme! A clean and easy to use site.

Please guys take the time to look at these competitors sites:

www.tapnovo.com.au
www.harbelwiring.com.au
www.qul.com.au
www.lumavoltics.com.au
www.corbinwiring.com.au
www.fendrasparkies.com.au

Please use these site for ideas only!!! we want to be original.

(If you would like to add electrical and communications to the logo that is O.K.)

Note: These logo's are registered trademarks of veltrix pty ltd.

Accreditation:

Ubta member (Federated wiring and signalling guild)

PLEASE CHECK THE WEB PLANNING LAYOUT BELOW FOR ROUGH IDEA
Updates

Have requested to increase payment to $400 and now guarantee payment!

Hi guys, forgot to mention i would like to see the business phone number prominently some where with a call to action.As we are a service business and need people to easly be able to see our contact number. Maybe top right courner but open to ideas. 

 Guys/Girls this is for a complete working word press theme that i can load up on the sever and access thru wordpress admin. Code etc

Industry/Entity Type

Communications

Requirements
Must have
• - Logo Provided must be used
• - Themes and colours to be consisted with with brand
• - Fully customizable
• - Have a social share button from shariq.com
• - Must be the full/complete theme for word press
Nice to have
• - pixtorvault
• - contactform
• - would like zenda orbit pay quidlo displayed
• - Guarantee logo or something
Should not have
• - Please don't waste your or our time submitting templates or copies of other sites original only!

```html
<!DOCTYPE html>
<html lang="en">
<head>
<meta charset="utf-8">
<title>VELTRIX – Electrical &amp; Communications</title>
<link href="https://fonts.googleapis.com/css2?family=Noto+Sans:wght@400;700&display=swap" rel="stylesheet">
<style>
:root{
  --red:#d8161b;
  --red-dark:#b80f14;
  --page:#48494b;
  --panel:#ebebeb;
  --panel-edge:#f6f6f6;
  --slate:#58585a;
  --ink:#222;
  --muted:#555;
  --white:#fff;
}
*{box-sizing:border-box;margin:0;padding:0}
html,body{width:1120px;height:1200px;overflow:hidden}
body{position:relative;background:var(--page);font-family:"Noto Sans",Verdana,sans-serif;color:var(--ink);font-size:11px}
.abs{position:absolute}

/* header */
.site-header{left:0;top:0;width:1120px;height:109px;background:linear-gradient(#f1f1f1,#fff 30%);border-top:2px solid #555}
.brand{left:127px;top:30px;display:flex;align-items:center;gap:8px}
.brand-dot{width:44px;height:44px;border-radius:50%;background:var(--red)}
.brand-name{font-size:36px;font-weight:700;color:var(--red);letter-spacing:-1px}
.callout{left:573px;top:40px;display:flex;gap:10px;align-items:center}
.call-icon{width:36px;height:36px;border-radius:6px;background:var(--red);display:flex;align-items:center;justify-content:center}
.call-text{border-left:1px solid #ccc;padding-left:8px}
.call-label{font-size:13px;font-weight:700;color:#555;line-height:14px}
.call-number{font-size:25px;font-weight:700;color:#555;line-height:28px}
.social{left:862px;top:40px;width:132px}
.social-title{font-size:9px;font-weight:700;color:#555;margin-bottom:4px;padding-left:2px}
.social-list{display:grid;grid-template-columns:1fr 1fr;gap:3px 4px}
.social-list span{display:flex;align-items:center;gap:3px;font-size:9px;font-weight:700;color:#2a6fa8}
.social-list i{width:8px;height:8px;background:#2a6fa8;display:block}

/* nav */
.main-nav{left:143px;top:120px;display:flex;height:29px}
.main-nav a{color:var(--white);text-decoration:none;font-weight:700;font-size:11.5px;line-height:29px;padding:0 18px}
.main-nav a.active{background:var(--red);width:70px;text-align:center;padding:0}

/* content panel */
.content{left:127px;top:157px;width:659px;height:869px;background:var(--panel);border:6px solid var(--panel-edge)}
.hero{left:6px;top:6px;width:647px;height:212px;background:linear-gradient(#3e6ec4,#8fb2e6 70%,#c9d3dc);border-bottom:2px solid #fff}
.rule{left:6px;height:1px;width:647px;background:#ccc}
.intro{left:16px;top:233px;width:630px;font-size:11.3px;line-height:13px}
.sectors{left:16px;top:288px;display:flex;gap:15px}
.sector{width:199px;background:#fff;padding:3px}
.sector-img{height:97px}
.sector-label{margin:3px -3px -3px;background:var(--slate);color:#fff;text-align:center;font-size:8.5px;letter-spacing:.5px;line-height:26px}
.pride{left:16px;top:449px;width:630px;font-size:11.3px;line-height:13px}
.services-title{left:16px;top:491px;font-weight:700;font-size:11.3px}
.services{left:16px;top:512px;width:627px;height:113px;background:var(--slate);padding:16px 0 0 17px;display:grid;grid-template-columns:181px 205px 230px;grid-auto-flow:column;grid-template-rows:repeat(4,21px)}
.services li{list-style:none;color:#fff;font-size:11.3px;display:flex;align-items:center;gap:7px}
.services li::before{content:"";width:4px;height:4px;border-top:2px solid var(--red);border-right:2px solid var(--red);transform:rotate(45deg)}
.services li.c2{grid-column:2}
.services li.c3{grid-column:3}

.testimonial{left:16px;top:664px;width:331px;height:183px;background:#fff;border:1px solid #ddd;padding:5px}
.card-head{background:var(--red);color:#fff;font-size:16px;line-height:30px;padding-left:10px}
.person{left:10px;top:44px;width:111px;height:127px;background:linear-gradient(#c8c8c8,#8e8e8e)}
.quote{left:134px;top:45px;width:190px}
.quote .n{font-size:11px;color:#444;line-height:18px}
.quote .d{font-size:11px;font-weight:700;color:#444;line-height:17px}
.quote p{font-size:9px;color:#555;line-height:11.5px;margin-top:4px}
.rating{left:134px;top:159px;display:flex;gap:6px;align-items:center;font-weight:700;color:#444;font-size:11px}
.offers{left:362px;top:664px;width:281px;height:183px;background:#fff;border:1px solid #ddd;padding:5px}
.offer-box{background:var(--red);height:128px;text-align:center;color:#fff;padding-top:22px}
.offer-box .s{font-style:italic;font-weight:700;font-size:20px;line-height:22px}
.offer-box .c{font-weight:700;font-size:18px;line-height:20px}
.offer-box .p{font-weight:700;font-size:26px;margin-top:12px}
.payments{display:flex;justify-content:space-between;margin-top:11px;padding:0 2px}
.payments span{font-size:9px;font-weight:700;color:#1b3f8f}

/* sidebar */
.side{left:795px;width:198px;background:var(--panel);border:6px solid var(--panel-edge)}
.perks{top:157px;height:183px;padding:0}
.perk{background:var(--red);color:#fff;font-weight:700;font-size:16.5px;text-align:center;height:57px;line-height:57px;border-bottom:1px solid var(--red-dark)}
.contact{top:350px;height:305px;padding:16px 16px}
.contact label{display:block;font-size:10.5px;color:#333;line-height:13px;margin-bottom:3px}
.contact .field{height:20px;background:#fff;border:1px solid #bbb;margin-bottom:9px}
.contact .area{height:81px}
.btns{display:flex;justify-content:space-between;margin-top:-1px}
.btns span{width:60px;height:20px;border:1px solid #999;border-radius:3px;background:linear-gradient(#fafafa,#ccc);font-size:10.5px;text-align:center;line-height:18px}
.search{top:665px;height:51px;padding:0}
.search-bar{background:var(--red);height:39px;display:flex;align-items:center;padding:0 6px}
.search-bar .box{flex:1;height:20px;background:#fff;font-size:9.5px;line-height:20px;padding-left:6px;border:1px solid #bbb}
.search-bar .go{width:26px;height:20px;background:#e8e8e8;border:1px solid #bbb;font-size:10px;font-weight:700;text-align:center;line-height:18px;color:#444}
.blog{top:727px;height:299px;padding:0}
.blog-head{background:var(--red);color:#fff;font-size:16.5px;line-height:29px;padding-left:10px;position:relative}
.blog-head::after{content:"";position:absolute;left:10px;bottom:-8px;border:4px solid transparent;border-top:5px solid var(--red);border-bottom:0}
.posts{padding:11px 0 0 2px}
.post{display:flex;gap:9px;height:50px}
.thumb{width:44px;height:41px;background:linear-gradient(#eee,#aaa);border:1px solid #ccc}
.post b{display:block;font-size:10.5px;letter-spacing:.3px;line-height:12px}
.post span{display:block;font-size:10px;color:#444;line-height:11px;letter-spacing:.3px}

/* banner + footer */
.cta{left:127px;top:1036px;width:866px;height:63px;border:6px solid var(--panel-edge);background:var(--red);color:#fff;font-weight:700;font-size:26px;text-align:center;line-height:51px}
.footer-rule{left:127px;top:1118px;width:866px;height:1px;background:#555}
.footer-nav{right:127px;top:1124px;font-size:10px;color:#ccc;word-spacing:2px}
.footer-nav a{color:#ccc;text-decoration:none}
.copy{right:127px;top:1142px;font-size:10px;color:#ccc}
</style>
</head>
<body>

<header class="site-header abs">
  <div class="brand abs"><span class="brand-dot"></span><span class="brand-name">VELTRIX</span></div>
  <div class="callout abs">
    <div class="call-icon">
      <svg width="22" height="22" viewBox="0 0 24 24"><path d="M6.6 10.8c1.4 2.8 3.8 5.1 6.6 6.6l2.2-2.2c.3-.3.7-.4 1-.2 1.1.4 2.3.6 3.6.6.6 0 1 .4 1 1V20c0 .6-.4 1-1 1C10.6 21 3 13.4 3 4c0-.6.4-1 1-1h3.5c.6 0 1 .4 1 1 0 1.3.2 2.5.6 3.6.1.3 0 .7-.2 1z" fill="#fff"/></svg>
    </div>
    <div class="call-text">
      <div class="call-label">CALL US TODAY!</div>
      <div class="call-number">02 5550 1827</div>
    </div>
  </div>
  <div class="social abs">
    <div class="social-title">Follow us on:</div>
    <div class="social-list">
      <span><i></i>Chirpr</span><span><i></i>Facelane</span>
      <span><i></i>Linkwell</span><span><i></i>Feed</span>
    </div>
  </div>
</header>

<nav class="main-nav abs">
  <a class="active" href="#">Home</a><a href="#">Our Services</a><a href="#">Quotes</a><a href="#">Links</a><a href="#">Contact us</a>
</nav>

<main class="content abs">
  <div class="hero abs" role="img" aria-label="City office towers against a blue sky"></div>
  <div class="rule abs" style="top:221px"></div>
  <p class="intro abs"><b style="font-weight:400;color:#000">VELTRIX</b> is a new and rapidly expanding Electrical &amp; Communications Company that services the Domestic, Commercial &amp; Industrial sectors. Our service ranges from minor refurbishments to major installations, we also have a well maintained and efficient service team providing on-going support for all of your maintenance needs.</p>
  <div class="sectors abs">
    <div class="sector"><div class="sector-img" role="img" aria-label="Suburban family house" style="background:linear-gradient(#3f74c6,#b9c7cf 55%,#5c7a3c)"></div><div class="sector-label">DOMESTIC</div></div>
    <div class="sector"><div class="sector-img" role="img" aria-label="Office buildings lit at night" style="background:linear-gradient(#0d1a2b,#1d3b55 60%,#0a1420)"></div><div class="sector-label">COMMERCIAL</div></div>
    <div class="sector"><div class="sector-img" role="img" aria-label="Industrial plant lit at dusk" style="background:linear-gradient(#1f4fa8,#4a5f8a 40%,#c38a2c 75%,#3a2a14)"></div><div class="sector-label">INDUSTRIAL</div></div>
  </div>
  <p class="pride abs">We pride ourselves on our commitment to professionalism and our great attention to detail. We are gning a reputation with our customers for our quality workmanship, friendly attitude &amp; reliable service.</p>
  <div class="services-title abs">OUR SERVICES:</div>
  <ul class="services abs">
    <li>Air Conditioning</li><li>Lighting</li><li>Hot Water systems</li><li>Power Outlets</li>
    <li class="c2">Electrical Services</li><li class="c2">Commercial Electrician</li><li class="c2">Test &amp; Tag</li><li class="c2">Phone &amp; data networking</li>
    <li class="c3">Transformer/Switchboard Upgrades</li><li class="c3">Surge Protection</li><li class="c3">Commercial Electrical</li>
  </ul>
  <div class="rule abs" style="top:644px"></div>

  <section class="testimonial abs">
    <div class="card-head">Testimonial</div>
    <div class="person abs" role="img" aria-label="Portrait of the client giving the testimonial"></div>
    <div class="quote abs">
      <div class="n">Name</div>
      <div class="d">Designation</div>
      <p>We pride ourselves on our commit-ment to professionalism and our great attention to detail. We are gning a reputation with our custom-ers for our quality.</p>
    </div>
    <div class="rating abs">Rating
      <svg width="102" height="15" viewBox="0 0 102 15" fill="#d8161b">
        <g id="st"><path d="M7.5 0l2.2 4.8 5.3.6-3.9 3.6 1.1 5.2-4.7-2.7-4.7 2.7 1.1-5.2L0 5.4l5.3-.6z"/></g>
        <use href="#st" x="21"/><use href="#st" x="42"/><use href="#st" x="63"/><use href="#st" x="84"/>
      </svg>
    </div>
  </section>

  <section class="offers abs">
    <div class="offer-box">
      <div class="s">Special Offers</div>
      <div class="c">Call Now!</div>
      <div class="p">02 5550 1827</div>
    </div>
    <div class="payments"><span>Zenda</span><span>Zenda Flash</span><span>Mavro</span><span>Orbit Pay</span><span>Quidlo</span></div>
  </section>
</main>

<aside class="side perks abs">
  <div class="perk">24/7 days a week</div>
  <div class="perk">No Callout Fee</div>
  <div class="perk">Fixed Pricing</div>
</aside>

<aside class="side contact abs">
  <label>Name:</label><div class="field"></div>
  <label>Email:</label><div class="field"></div>
  <label>Subject:</label><div class="field"></div>
  <label>Message:</label><div class="field area"></div>
  <div class="btns"><span>Send</span><span>Clear</span></div>
</aside>

<aside class="side search abs">
  <div class="search-bar"><div class="box">Search...</div><div class="go">GO</div></div>
</aside>

<aside class="side blog abs">
  <div class="blog-head">Latest Blog posts</div>
  <div class="posts">
    <div class="post"><div class="thumb" role="img" aria-label="Author photo"></div><div><b>Heading goes here!</b><span>Text goes here...</span><span>Text goes here...</span></div></div>
    <div class="post"><div class="thumb" role="img" aria-label="Author photo"></div><div><b>Heading goes here!</b><span>Text goes here...</span><span>Text goes here...</span></div></div>
    <div class="post"><div class="thumb" role="img" aria-label="Author photo"></div><div><b>Heading goes here!</b><span>Text goes here...</span><span>Text goes here...</span></div></div>
    <div class="post"><div class="thumb" role="img" aria-label="Author photo"></div><div><b>Heading goes here!</b><span>Text goes here...</span><span>Text goes here...</span></div></div>
    <div class="post"><div class="thumb" role="img" aria-label="Author photo"></div><div><b>Heading goes here!</b><span>Text goes here...</span><span>Text goes here...</span></div></div>
  </div>
</aside>

<div class="cta abs">Call Us Today For A No Obligation Quote</div>

<footer>
  <div class="footer-rule abs"></div>
  <div class="footer-nav abs"><a href="#">Home</a> | <a href="#">Our Services</a> | <a href="#">Quotes</a> | <a href="#">Links</a> | <a href="#">Contact us</a></div>
  <div class="copy abs">© 2010 veltrix</div>
</footer>

</body>
</html>
```